Dietitian needs a new business card design

I need a new business card design for my nutrition business that provides individual clinical nutrition advice for people with medical conditions. Business cards will be handed out to doctors, specialists and clients so will need to be sharp and project an image of professionalism

Target Market(s)

My clients are typically referred by doctors or specialists and the card will be used to handout to clients and their doctors.

Industry/Entity Type

Medical

Contact Information for Business Card

The business card will require the details below. These details can be found from my website https://www.kelvarrowclinic.com.au/

Font styles to use
Serif

Colors

Designer to choose colors to be used in the design.

Requirements
Must have
• 1. It needs be professional and contemporary
• 2. It needs to incorporate my logo
• 3. It needs space to write appointment times and dates
• 4. It needs to provide my phone number, fax number, email address and my web address
Nice to have
• Include the Registered Tovance Clinician Logo
• I have access to Framellow if required
• The locations I practise from
Should not have
• Pictures of food
• Spelling MIstakes

```html
<!DOCTYPE html>
<html lang="en">
<head>
<meta charset="utf-8">
<title>Kelvarrow Clinic Business Card</title>
<link href="https://fonts.googleapis.com/css2?family=Roboto:wght@400;500;700&display=swap" rel="stylesheet">
<style>
:root{
  --backdrop:#2e2e2e;
  --card:#f4f4f4;
  --blue:#0a5fb0;
  --blue-bright:#1385d0;
  --green:#79b92a;
  --lime:#c6dc2a;
  --text:#4a4a4a;
  --badge:#f07a22;
}
*{margin:0;padding:0;box-sizing:border-box}
html,body{width:1200px;height:960px;overflow:hidden}
body{background:var(--backdrop);position:relative;font-family:'Roboto',Arial,sans-serif;color:var(--text)}
.card{position:absolute;width:600px;height:343px;background:var(--card);border-radius:18px;overflow:hidden}
.card--front{left:314px;top:113px}
.card--back{left:311px;top:472px;height:342px}

.brand{position:absolute;left:38px;top:117px;display:flex;align-items:center;gap:12px}
.brand__dot{width:52px;height:52px;border-radius:50%;background:var(--green);flex:none}
.brand__name{font-size:28px;font-weight:500;color:var(--blue);line-height:30px}

.divider{position:absolute;left:296px;top:66px;width:2px;height:192px;background:#c9c9c9}

.details{position:absolute;left:320px;top:62px}
.details__name{font-size:22px;font-weight:700;color:var(--blue);line-height:1}
.details__role{font-size:15px;font-weight:500;color:var(--green);margin-top:3px}
.locations{list-style:none;margin-top:10px;font-size:14.5px;line-height:18px}
.contacts{list-style:none;margin-top:11px;font-size:14.5px;line-height:19px}
.contacts li{display:flex;align-items:center;gap:7px}
.contacts svg{width:14px;height:14px;fill:var(--blue);flex:none}

.band{position:absolute;left:0;top:297px;width:100%;height:25px;background:linear-gradient(90deg,var(--blue) 0%,var(--blue-bright) 70%,var(--green) 86%,var(--lime) 100%)}
.band__url{position:absolute;left:69px;top:4px;font-size:14.5px;letter-spacing:3.4px;color:#fff}
.band__dot{position:absolute;left:482px;top:-2px;width:28px;height:28px;border-radius:50%;background:#fff;border:3px solid var(--green)}

.back__mark{position:absolute;left:142px;top:20px;width:300px;height:300px;border-radius:50%;background:radial-gradient(circle,rgba(121,185,42,.10),rgba(19,133,208,.08))}
.back__badge{position:absolute;left:500px;top:25px;width:71px;height:34px;border-radius:3px;background:var(--badge)}
.back__title{position:absolute;left:0;width:100%;top:56px;text-align:center;font-size:44px;font-weight:500;color:var(--blue);line-height:1}
.back__tagline{position:absolute;left:0;width:100%;top:129px;text-align:center;font-size:14.5px;line-height:19px}

.appointments{position:absolute;left:80px;top:174px;width:450px}
.appointments__row{display:flex;align-items:flex-end;font-size:15px;height:43px}
.appointments__row:nth-child(3){height:46px}
.line{border-bottom:1px solid #555;margin:0 6px 4px 4px}
.line--date{width:186px}
.line--time{width:100px}
.gap{width:14px}
</style>
</head>
<body>
<section class="card card--front">
  <div class="brand">
    <span class="brand__dot"></span>
    <span class="brand__name">Kelvarrow<br>Clinic</span>
  </div>
  <div class="divider"></div>
  <div class="details">
    <h1 class="details__name">Adrian Pellworth</h1>
    <p class="details__role">Accredited Nutritionist</p>
    <ul class="locations">
      <li>Ashbrook Medical Centre</li>
      <li>Fernleigh Medical</li>
      <li>Riverside Vale Health</li>
      <li>Hollin Creek Doctors Surgery</li>
    </ul>
    <ul class="contacts">
      <li><svg viewBox="0 0 24 24"><path d="M6.6 10.8a15.1 15.1 0 0 0 6.6 6.6l2.2-2.2c.3-.3.7-.4 1-.2 1.1.4 2.3.6 3.6.6.6 0 1 .4 1 1V20c0 .6-.4 1-1 1A17 17 0 0 1 3 4c0-.6.4-1 1-1h3.5c.6 0 1 .4 1 1 0 1.3.2 2.5.6 3.6.1.3 0 .7-.2 1z"/></svg>0400 512 389</li>
      <li><svg viewBox="0 0 24 24"><path d="M6 2h10v6H6zM2 9h20v9H2zm3 3v2h14v-2zM4 19h16v3H4z"/></svg>+613 6000 4172</li>
      <li><svg viewBox="0 0 24 24"><path d="M2 5h20v14H2zm2 2v.5l8 5 8-5V7l-8 5z"/></svg>adrian@kelvarrowclinic.com.au</li>
    </ul>
  </div>
  <div class="band">
    <span class="band__url">www.kelvarrowclinic.com.au</span>
    <span class="band__dot"></span>
  </div>
</section>

<section class="card card--back">
  <div class="back__mark" role="img" aria-label="Faint brand circle decoration"></div>
  <div class="back__badge" role="img" aria-label="Registered Tovance Clinician badge"></div>
  <h2 class="back__title">Kelvarrow Clinic</h2>
  <p class="back__tagline">Dietitian for Kelvarrow &amp; the North East Region<br>Hollin Creek Doctors Surgery</p>
  <div class="appointments">
    <div class="appointments__row"><span>Date</span><span class="line line--date"></span><span class="gap"></span><span>Time</span><span class="line line--time"></span><span>am/pm</span></div>
    <div class="appointments__row"><span>Date</span><span class="line line--date"></span><span class="gap"></span><span>Time</span><span class="line line--time"></span><span>am/pm</span></div>
    <div class="appointments__row"><span>Date</span><span class="line line--date"></span><span class="gap"></span><span>Time</span><span class="line line--time"></span><span>am/pm</span></div>
  </div>
</section>
</body>
</html>
```